Banner Ad Needed For Real Estate Lending Firm

We are taking out a banner ad on one of the most highly trafficked real estate websites in New York. The ad will be 970x250. Display format will be JPEG or animated GIF, but original art files will be required as well from the winning designer.

Harbor Ridge Lending (or HRL) is one of the largest "hard money lenders" for real estate investors on the East Coast of the US. We lend for the following real estate investments: 1) Fix And Flip 2) New Construction 3) Cash Out Refinance. We close in 2-10 days. More information can be found on our website here: http://www.hrl7-example.net/

Our goal is to help small business owners, real estate investors, and commercial contractors quickly and efficiently finance their business activities. Our local hard money loan programs are tailored to your unique project needs. We fund fix and flip, new construction, and cash out refinance projects for non-owner occupied properties.

Target Market(s)

Real Estate Agents, Real Estate Investors, Mortgage Brokers, Other Real Estate Professionals

Industry/Entity Type

Real Estate

Font styles to use
Sans Serif

Requirements
Must have
• Must incorporate the fact that we close deals very fast (2 - 10 days), finance the following these 2 main types of investments (Fix and Flip, New Construction), and mention that Brokers can make up to 2.5 Points.
• See attached style guide for basic colors and fonts.
Nice to have
• Animated GIF might be a great feature!

```html
<!DOCTYPE html>
<html lang="en">
<head>
<meta charset="utf-8">
<title>Harbor Ridge Lending – Banner Frames</title>
<link rel="stylesheet" href="https://fonts.googleapis.com/css2?family=Figtree:wght@400;600;700;800&display=swap">
<style>
  :root{
    --page-red:#d93236;
    --label-pink:#f08a86;
    --teal:#07505f;
    --ink-teal:#0b4f5e;
    --accent-red:#d93236;
    --orange:#f5a422;
    --green:#8cc63f;
    --white:#ffffff;
    --photo-dark:#3a3634;
    --photo-warm:#7a5646;
  }
  *{box-sizing:border-box;margin:0;padding:0}
  html,body{width:1062px;height:1200px;overflow:hidden}
  body{background:var(--page-red);font-family:"Figtree",Arial,sans-serif;position:relative}
  .frame-label{position:absolute;left:42px;width:24px;color:var(--label-pink);font-size:20px;font-weight:600;
    transform:rotate(-90deg);transform-origin:center;white-space:nowrap;display:flex;justify-content:center}
  .banner{position:absolute;left:81px;width:896px;height:231px;overflow:hidden}
  .banner-shapes{position:absolute;inset:0;width:100%;height:100%}
  .brand{position:absolute;left:22px;top:30px;display:flex;align-items:center;gap:12px}
  .brand-mark{width:22px;height:22px;background:var(--white)}
  .brand-name{color:var(--white);font-weight:700;font-size:23px;line-height:30px;text-transform:uppercase;letter-spacing:.2px}
  .contact-phone{position:absolute;left:0;width:330px;top:143px;text-align:center;color:var(--orange);
    font-weight:800;font-size:34px;letter-spacing:.5px}
  .contact-email{position:absolute;left:0;width:330px;top:190px;text-align:center;color:var(--orange);
    font-weight:700;font-size:19px;letter-spacing:1px}
  .pitch{position:absolute;left:340px;width:270px;top:20px;text-align:center;color:var(--white);
    font-size:29px;line-height:39px;font-weight:400}
  .pitch .hl-orange{color:var(--orange)}
  .pitch .hl-green{color:var(--green)}
  .offer{position:absolute;left:620px;width:296px;top:0;height:231px;display:flex;flex-direction:column;
    justify-content:center;align-items:center;text-align:center;color:var(--ink-teal);font-weight:600;text-transform:uppercase}
  .offer .accent{color:var(--accent-red)}
</style>
</head>
<body>

<!-- Frame 1 -->
<div class="frame-label" style="top:185px">FRAME 1</div>
<section class="banner" style="top:75px">
  <svg class="banner-shapes" viewBox="0 0 896 231" preserveAspectRatio="none">
    <defs><linearGradient id="photoTone" x1="0" y1="0" x2="1" y2="1">
      <stop offset="0" stop-color="#8a5e4c"/><stop offset=".55" stop-color="#3c3735"/><stop offset="1" stop-color="#5a4a3e"/></linearGradient></defs>
    <rect x="0" y="0" width="380" height="231" fill="url(#photoTone)" role="img" aria-label="Photo of a smiling builder laying bricks on a construction site"/>
    <polygon points="362,0 896,0 896,231 316,231" fill="#07505f"/>
    <polygon points="658,0 896,0 896,231 611,231" fill="#ffffff"/>
  </svg>
  <div class="brand"><span class="brand-mark"></span><div class="brand-name">Harbor Ridge<br>Lending LLC</div></div>
  <div class="contact-phone">555.010.4827</div>
  <div class="contact-email">info@hrl7-example.net</div>
  <p class="pitch">HRL is the<br><span class="hl-orange">leading</span> hard<br>money lender<br>to <span class="hl-green">local</span> real<br>estate investors.</p>
  <div class="offer">
    <div style="font-size:31px;line-height:44px">We close<br>deals very</div>
    <div class="accent" style="font-size:63px;line-height:62px;font-weight:700">Fast</div>
    <div style="font-size:31px;line-height:44px">(2 - 10 days)</div>
  </div>
</section>

<!-- Frame 2 -->
<div class="frame-label" style="top:459px">FRAME 2</div>
<section class="banner" style="top:349px">
  <svg class="banner-shapes" viewBox="0 0 896 231" preserveAspectRatio="none">
    <rect x="0" y="0" width="380" height="231" fill="url(#photoTone)" role="img" aria-label="Photo of a smiling builder laying bricks on a construction site"/>
    <polygon points="362,0 896,0 896,231 316,231" fill="#07505f"/>
    <polygon points="658,0 896,0 896,231 611,231" fill="#ffffff"/>
  </svg>
  <div class="brand"><span class="brand-mark"></span><div class="brand-name">Harbor Ridge<br>Lending LLC</div></div>
  <div class="contact-phone">555.010.4827</div>
  <div class="contact-email">info@hrl7-example.net</div>
  <p class="pitch">HRL is the<br><span class="hl-orange">leading</span> hard<br>money lender<br>to <span class="hl-green">local</span> real<br>estate investors.</p>
  <div class="offer">
    <div style="font-size:31px;line-height:46px">We fund</div>
    <div class="accent" style="font-size:49px;line-height:62px">Fix &amp; Flip</div>
    <div style="font-size:31px;line-height:46px">Hard money<br>loans</div>
  </div>
</section>

<!-- Frame 3 -->
<div class="frame-label" style="top:734px">FRAME 3</div>
<section class="banner" style="top:624px">
  <svg class="banner-shapes" viewBox="0 0 896 231" preserveAspectRatio="none">
    <rect x="0" y="0" width="380" height="231" fill="url(#photoTone)" role="img" aria-label="Photo of a smiling builder laying bricks on a construction site"/>
    <polygon points="362,0 896,0 896,231 316,231" fill="#07505f"/>
    <polygon points="658,0 896,0 896,231 611,231" fill="#ffffff"/>
  </svg>
  <div class="brand"><span class="brand-mark"></span><div class="brand-name">Harbor Ridge<br>Lending LLC</div></div>
  <div class="contact-phone">555.010.4827</div>
  <div class="contact-email">info@hrl7-example.net</div>
  <p class="pitch">HRL is the<br><span class="hl-orange">leading</span> hard<br>money lender<br>to <span class="hl-green">local</span> real<br>estate investors.</p>
  <div class="offer" style="left:612px">
    <div style="font-size:31px;line-height:40px">We fund</div>
    <div class="accent" style="font-size:29px;line-height:40px">New<br>construction</div>
    <div style="font-size:31px;line-height:40px">Hard money<br>loans</div>
  </div>
</section>

<!-- Frame 4 -->
<div class="frame-label" style="top:1008px">FRAME 4</div>
<section class="banner" style="top:899px">
  <svg class="banner-shapes" viewBox="0 0 896 231" preserveAspectRatio="none">
    <rect x="0" y="0" width="380" height="231" fill="url(#photoTone)" role="img" aria-label="Photo of a smiling builder laying bricks on a construction site"/>
    <polygon points="362,0 896,0 896,231 316,231" fill="#07505f"/>
    <polygon points="658,0 896,0 896,231 611,231" fill="#ffffff"/>
  </svg>
  <div class="brand"><span class="brand-mark"></span><div class="brand-name">Harbor Ridge<br>Lending LLC</div></div>
  <div class="contact-phone">555.010.4827</div>
  <div class="contact-email">info@hrl7-example.net</div>
  <p class="pitch">HRL is the<br><span class="hl-orange">leading</span> hard<br>money lender<br>to <span class="hl-green">local</span> real<br>estate investors.</p>
  <div class="offer" style="left:610px">
    <div style="font-size:31px;line-height:48px">Brokers<br>can make<br>up to</div>
    <div class="accent" style="font-size:43px;line-height:54px">2.5 Points</div>
  </div>
</section>

</body>
</html>
```